依頼詳細
頂いている参考サイトとしては下記のURLがありますが、
先方でもどのデザインの何が良いのかは計りかねているらしく、
下記を参考に様々な形式でデザインを作成して欲しいということです。

‣BRIGHTLEAF https://www.brightleaf57.jp/biwako-sup/ ➡デザインが素敵
‣丸岡商 https://www.maruokasho.co.jp/ja/ ➡ 大企業感
‣ひらめき工房本部 https://www.hiramekikobo.jp/  ➡ 同コンセプト

また、事業内容は現在のページに準拠するということで、現在サイトのパスはpemixとなります。

TOPページへの掲載内容については、
TOPイメージ
事業内容
採用情報
新着情報
となります。
サイトURL
http://nexal.co.jp/
ページ数
1ページ
希望イメージ
シンプル 複雑
単色 カラフル
暗い 明るい
日常 高級
遊び心 厳粛
未来的 伝統的
女性的 男性的
希望する色
緑系
納品ファイル
• フォトショップ形式 (.psd)
補足説明
依頼公開後の追記内容
現行サイトのパスワードについて失念しておりました。
パスワードは pemix となります。
■ 選んだ理由

デザインが特に先方に気に入られたため

■ 提案者全員のお礼・コメント

この度はご提案をいただきまして、誠にありがとうございました。
また機会がありましたら、よろしくお願い致します。

```html
<!DOCTYPE html>
<html lang="ja">
<head>
<meta charset="utf-8">
<title>株式会社ネクサル</title>
<link href="https://fonts.googleapis.com/css2?family=Noto+Sans+JP:wght@400;500;700;900&family=Roboto:wght@500;700&display=swap" rel="stylesheet">
<style>
:root{
  --green:#22b14c;
  --green-dark:#169a3c;
  --green-deep:#0f8a32;
  --mint:#eef8ea;
  --blue:#1c6db5;
  --ink:#333;
  --muted:#666;
  --white:#fff;
}
*{margin:0;padding:0;box-sizing:border-box}
html,body{width:1200px;height:3100px;overflow:hidden}
body{font-family:"Noto Sans JP",sans-serif;color:var(--ink);background:var(--white);position:relative}
.abs{position:absolute}
.en{font-family:"Roboto",sans-serif;letter-spacing:.08em}

/* hero */
.hero{left:0;top:0;width:1200px;height:580px;overflow:hidden}
.hero-photo{position:absolute;inset:0;background:linear-gradient(100deg,#c9d3d9 0%,#dfe6ea 40%,#f1efe9 62%,#e7e0d8 100%)}
.hero-photo::after{content:"";position:absolute;left:640px;top:60px;width:380px;height:540px;border-radius:180px 180px 0 0;background:linear-gradient(180deg,#b9a28d 0%,#eef0f3 45%,#9db0c4 100%);opacity:.55}
.logo{left:36px;top:30px;display:flex;align-items:center;gap:10px}
.logo-mark{width:30px;height:30px;background:var(--green);border-radius:4px}
.logo-name{font-weight:700;font-size:22px;color:var(--green)}
.menu-btn{right:36px;top:24px;width:44px;height:44px;border-radius:50%;background:var(--green)}
.hero-copy{left:100px;top:250px;color:var(--white);font-weight:900;font-size:50px;line-height:1.5;letter-spacing:.08em;text-shadow:0 2px 8px rgba(0,0,0,.25)}
.hero-copy .em{color:#c9f5b5}
.hero-wave{left:0;top:500px;width:1200px;height:90px}

/* section titles */
.sec-title{left:0;width:1200px;text-align:center}
.sec-title h2{font-size:30px;font-weight:700;letter-spacing:.1em}
.sec-title .en{display:block;font-size:14px;color:var(--green);margin-top:4px}
.sec-title .bar{display:block;width:60px;height:3px;background:var(--green);margin:4px auto 0}

/* news */
.news{left:140px;top:800px;width:920px;list-style:none}
.news li{display:flex;align-items:center;gap:22px;height:58px;border-bottom:1px solid #e2e2e2;font-size:15px}
.news .dot{width:16px;height:16px;border-radius:50%;background:var(--green);position:relative;flex:none}
.news .dot::after{content:"";position:absolute;left:5px;top:5px;width:5px;height:5px;border-top:2px solid #fff;border-right:2px solid #fff;transform:rotate(45deg) translate(-1px,1px)}
.news time{font-family:"Roboto",sans-serif;color:var(--muted);width:100px;flex:none}

.pill{display:inline-flex;align-items:center;justify-content:center;gap:14px;height:44px;border-radius:22px;font-size:14px;font-weight:500;padding:0 34px}
.pill::after{content:"→"}
.pill.outline{border:2px solid var(--green);color:var(--green);background:#fff}
.pill.white{background:#fff;color:var(--green)}
.pill.white.blue{color:var(--blue)}

.divider{left:599px;top:1210px;width:2px;height:80px;background:var(--green)}

/* business */
.edu-photo{left:0;top:1420px;width:760px;height:390px;background:linear-gradient(120deg,#e8e2d8,#cdbfae 55%,#8d7b70)}
.edu-panel{left:0;top:1420px;width:1200px;height:390px}
.panel-text{color:#fff;text-align:center}
.panel-text h3{font-size:32px;font-weight:700;letter-spacing:.08em;margin-bottom:26px}
.panel-text p{font-size:15px;line-height:2}
.event-photo{left:500px;top:1840px;width:700px;height:380px;background:linear-gradient(135deg,#cfd7dd,#e9e3d6 50%,#b7c3cf)}

/* recruit */
.recruit-bg{left:0;top:2240px;width:1200px;height:560px;background:var(--mint)}
.recruit-photo{left:160px;top:2440px;width:480px;height:320px;background:linear-gradient(160deg,#c8d2dc,#eef1f4 50%,#7d8796)}
.recruit-card{left:600px;top:2480px;width:440px;height:300px;background:#fff;padding:30px 40px;border-left:6px solid var(--green)}
.recruit-card h3{font-size:20px;color:var(--green);margin-bottom:18px}
.recruit-card p{font-size:14px;line-height:2;color:var(--ink)}

/* footer */
.footer{left:0;top:2820px;width:1200px;height:240px;background:var(--green);color:#fff;text-align:center}
.footer h2{font-size:26px;font-weight:700;margin-top:36px;letter-spacing:.06em}
.footer .addr{font-size:13px;line-height:1.9;margin-top:12px}
.foot-nav{display:flex;justify-content:center;margin-top:22px;list-style:none;font-size:13px}
.foot-nav li{padding:0 34px;border-left:1px solid rgba(255,255,255,.6)}
.foot-nav li:first-child{border-left:none}
.copyright{left:0;top:3060px;width:1200px;height:40px;background:var(--green-deep);color:#fff;font-size:12px;text-align:center;line-height:40px}
</style>
</head>
<body>

<section class="abs hero">
  <div class="hero-photo" role="img" aria-label="本を抱えて空を見上げる学生の写真"></div>
  <div class="abs logo"><span class="logo-mark"></span><span class="logo-name">株式会社ネクサル</span></div>
  <div class="abs menu-btn"></div>
  <h1 class="abs hero-copy">子供たちの<span class="em">憧れる</span><br>かっこいい大人であれ</h1>
  <svg class="abs hero-wave" viewBox="0 0 1200 90" preserveAspectRatio="none"><path d="M0 50 L700 80 L1200 20 L1200 90 L0 90Z" fill="#fff"/><path d="M0 40 L700 72 L1200 12 L1200 20 L700 80 L0 50Z" fill="#22b14c" opacity=".5"/></svg>
</section>

<svg class="abs" style="left:0;top:580px" width="1200" height="640" viewBox="0 0 1200 640"><path d="M0 0 H260 L0 640Z" fill="#eef8ea"/><path d="M1200 380 V640 H1000Z" fill="#eef8ea"/></svg>

<div class="abs sec-title" style="top:630px"><h2>新着情報</h2><span class="en">NEWS</span><span class="bar"></span></div>
<ul class="abs news">
  <li><span class="dot"></span><time>2022.02.14</time>ホームページをリニューアルしました。</li>
  <li><span class="dot"></span><time>2022.02.10</time>新着情報のタイトルが入ります。</li>
  <li><span class="dot"></span><time>2022.02.02</time>新着情報のタイトルが入ります。新着情報のタイトルが入ります。</li>
</ul>
<a class="abs pill outline" style="left:500px;top:1050px;width:200px">新着情報一覧へ</a>

<div class="abs divider"></div>
<div class="abs sec-title" style="top:1320px"><h2>事業案内</h2><span class="en">INFORMATION</span><span class="bar"></span></div>

<div class="abs edu-photo" role="img" aria-label="机で勉強する制服姿の学生の写真"></div>
<svg class="abs edu-panel" viewBox="0 0 1200 390"><polygon points="760,0 1200,0 1200,390 700,390" fill="#22b14c"/><polygon points="690,40 760,0 700,390 650,390" fill="#169a3c" opacity=".5"/></svg>
<div class="abs panel-text" style="left:760px;top:1480px;width:420px">
  <h3>教育事業部</h3>
  <p>教育を基点とした地域活性化<br>「まなびの森スクール」<br>その他さまざまな学習を提供します。</p>
  <a class="pill white" style="margin-top:24px;width:220px">教育事業部へ</a>
</div>

<div class="abs event-photo" role="img" aria-label="机に広げた資料を囲む打ち合わせの写真"></div>
<svg class="abs" style="left:0;top:1840px" width="1200" height="380" viewBox="0 0 1200 380"><polygon points="100,10 640,10 580,300 100,300" fill="#1c6db5"/><polygon points="0,300 520,300 500,380 0,380" fill="#fff"/></svg>
<div class="abs panel-text" style="left:100px;top:1910px;width:460px">
  <h3>日祭事業部</h3>
  <p>様々な文化交流イベント、<br>事業によって、<br>日本にタイの文化を浸透させます。</p>
  <a class="pill white blue" style="margin-top:24px;width:220px">日祭事業部へ</a>
</div>

<div class="abs recruit-bg"></div>
<div class="abs sec-title" style="top:2330px"><h2>採用情報</h2><span class="en">RECRUIT</span><span class="bar"></span></div>
<div class="abs recruit-photo" role="img" aria-label="スーツ姿の男女二人の写真"></div>
<div class="abs recruit-card">
  <h3>求めるNEXAL人財</h3>
  <p>目の前の顧客の思いを真剣に取り添い、<br>NEXALのサービスを通じ、<br>夢や目標を達成するためのサポートに<br>喜びを感じられる人財に<br>是非挑戦していただきたいと思います。</p>
  <a class="pill outline" style="margin-top:18px;width:200px">採用情報へ</a>
</div>

<footer class="abs footer">
  <h2>株式会社 NEXAL</h2>
  <p class="addr">本社事務所<br>〒500-0000 岐阜県岐阜市緑町1-2-3 ネクサルビル3F<br>TEL：058-000-0000　FAX：058-000-0001</p>
  <ul class="foot-nav"><li>HOME</li><li>事業案内</li><li>採用情報</li><li>新着情報</li><li>会社概要</li><li>お問い合わせ</li></ul>
</footer>
<div class="abs copyright">© 2022 株式会社 NEXAL</div>

</body>
</html>
```